Spy/Espionage/Counterintelligence Membership Community Needs a PowerPoint Template

We need a powerpoint template for one of our business verticals focused on spies, espionage, and counterintelligence. The name of it is "Amber Harbor Guild" and the logo is attached. Amber Harbor Guild is a community that connects people with experts in espionage and counterintelligence through an online social network, as well as in-person events. We would like to see designs that incorporate the red and black of the logo. The design should communicate mystery/suspense and peak curiosity.

Target Market(s)

Late 20s to baby boomers, male

Industry/Entity Type

Social Club

Font styles to use
Sans Serif

Colors
ec1f27
000000
ffffff

Requirements
Must have
• A user-friendly ppt template file. Incorporate basic fonts that don't have to be installed on every computer for presentations. A cover slide and a basic inside slide. A white background. I will also need graphic source files.
Nice to have
• Plenty of space for slide title and body content. Logo on every slide.
Should not have
• Inconsistency with fonts. Misalignment of images.

```html
<!DOCTYPE html>
<html lang="en">
<head>
<meta charset="utf-8">
<title>Amber Harbor Guild – Presentation Template</title>
<link rel="stylesheet" href="https://fonts.googleapis.com/css2?family=Figtree:wght@400;500;600;700;800&display=swap">
<style>
  :root{
    --red:#d90d14;
    --red-soft:#e0383c;
    --ink:#3a3a3a;
    --black:#000;
    --white:#fff;
    --paper-top:#f7f7f7;
    --paper-bottom:#e4e4e4;
    --bar:#dcdcdc;
    --grey-dark:#4a4a4a;
    --grey-mid:#6a6a6a;
    --grey-light:#c9c9c9;
    --row:#efefef;
    --chev:#9a9a9a;
  }
  *{box-sizing:border-box;margin:0;padding:0}
  html,body{width:1061px;height:1200px;overflow:hidden;background:var(--black)}
  body{font-family:"Figtree",Arial,sans-serif;color:var(--ink);position:relative}

  .slide{position:absolute;width:518px;height:390px;overflow:hidden;
    background:linear-gradient(180deg,var(--paper-top),var(--paper-bottom));
    border-top:6px solid var(--red)}
  .col-left{left:8px}.col-right{left:536px}
  .row-1{top:8px}.row-2{top:407px}.row-3{top:804px}

  /* headings */
  .slide-title{position:absolute;left:24px;top:16px;font-size:30px;font-weight:700;color:var(--ink);letter-spacing:-.2px}
  .accent{color:var(--red)}

  /* brand lockup */
  .brand{display:flex;flex-direction:column;align-items:center;gap:4px}
  .brand-mark{width:50px;height:50px;border-radius:50%;background:var(--red);border:3px solid var(--black)}
  .brand-name{font-size:20px;font-weight:500;color:var(--black);letter-spacing:-.3px;white-space:nowrap}

  /* footer bar */
  .footer{position:absolute;left:0;right:0;bottom:0;height:34px;background:var(--bar)}
  .footer-tab{position:absolute;left:50%;transform:translateX(-50%);bottom:0;width:126px;height:38px;
    background:var(--red);border-radius:6px 6px 0 0;display:flex;flex-direction:column;align-items:center;justify-content:center;gap:2px}
  .footer-tab .dot{width:15px;height:15px;border-radius:50%;background:var(--white)}
  .footer-tab .name{font-size:11px;font-weight:500;color:var(--white);white-space:nowrap}
  .footer .chev{position:absolute;top:9px;width:10px;height:16px}
  .footer .chev.prev{left:calc(50% - 84px)}
  .footer .chev.next{left:calc(50% + 74px)}

  /* cover band */
  .band{position:absolute;left:0;right:0;bottom:0;height:108px;background:var(--red)}
  .band .arrow{position:absolute;top:14px;width:44px;height:80px}
  .band .arrow.prev{left:18px}.band .arrow.next{right:18px}
  .byline{position:absolute;left:0;right:0;top:34px;text-align:center;color:var(--white);font-size:15px;line-height:20px}
  .byline strong{display:block;font-size:17px;font-weight:700}

  /* cover */
  .cover-title{position:absolute;left:0;right:0;top:50px;text-align:center;font-size:50px;font-weight:800;letter-spacing:-.3px;line-height:54px}
  .cover-sub{position:absolute;left:0;right:0;top:108px;text-align:center;font-size:42px;font-weight:400;color:var(--ink);line-height:46px}
  .cover .brand{position:absolute;left:0;right:0;top:186px}

  /* about */
  .about-body{position:absolute;left:24px;right:22px;top:66px;font-size:13.8px;line-height:19px;text-align:justify;color:var(--ink)}
  .about-body p{margin-bottom:12px}
  .about-body b{color:var(--red);font-weight:600}

  /* services */
  .service-list{position:absolute;left:22px;top:66px;list-style:none}
  .service-list li{font-size:18.5px;font-weight:500;line-height:25px;display:flex;align-items:center;gap:12px}
  .service-list li::before{content:"";width:7px;height:7px;background:var(--red);transform:rotate(45deg)}
  .team-photo{position:absolute;left:228px;top:78px;width:236px;height:222px;border-radius:4px;
    background:linear-gradient(180deg,#e9e9e9,#3c3c44 55%,#25252a)}

  /* table */
  .data-table{position:absolute;left:24px;top:68px;width:469px;border-collapse:collapse;font-size:10px}
  .data-table th{height:25px;font-size:14px;font-weight:700}
  .data-table th.cat{background:var(--grey-light);color:var(--ink)}
  .data-table th.opt1{background:var(--red);color:var(--white)}
  .data-table th.opt2{background:var(--grey-dark);color:var(--white)}
  .data-table td{height:18px}
  .data-table tr.group td{background:var(--grey-light);font-weight:700;font-size:10.5px;padding-left:6px;color:var(--ink)}
  .data-table td.label{padding-left:30px;background:var(--white);color:var(--ink)}
  .data-table tr.alt td.label{background:var(--row)}
  .data-table td.yes{background:var(--red);color:var(--white);text-align:center}
  .data-table tr.alt td.yes{background:var(--red-soft)}
  .data-table td.no{background:var(--grey-dark);color:var(--white);text-align:center}
  .data-table tr.alt td.no{background:var(--grey-mid)}
  .data-table .c1{width:233px}.data-table .c2{width:117px}.data-table .c3{width:119px}

  /* contact */
  .map{position:absolute;left:31px;top:66px;width:222px;height:220px;border:5px solid var(--white);
    box-shadow:0 0 3px rgba(0,0,0,.25);background:linear-gradient(160deg,#dfe6c8 0%,#cfdcb4 45%,#a9c6de 70%,#8fb6d6 100%)}
  .contact-body{position:absolute;left:266px;top:64px;width:238px;font-size:9.8px;line-height:11.5px;color:var(--ink)}
  .contact-body .lead{text-align:justify;margin-bottom:6px}
  .contact-body .lead b{color:var(--red);font-weight:600}
  .contact-body h4{font-size:11.5px;color:var(--red);font-weight:600;margin-top:7px;line-height:14px}
  .social{position:absolute;left:31px;top:298px;display:flex;align-items:center;gap:8px}
  .social .sq{width:17px;height:17px;background:var(--red);border-radius:2px}
  .social .handle{font-size:11.5px;font-weight:500;color:var(--ink);margin-left:4px}
  .social .handle span{color:var(--red)}

  /* thank you */
  .thanks{position:absolute;left:0;right:0;top:70px;text-align:center;font-size:74px;font-weight:800;letter-spacing:-1.5px;color:var(--ink);line-height:80px}
  .closing .brand{position:absolute;left:0;right:0;top:176px}
</style>
</head>
<body>

<section class="slide cover col-left row-1">
  <h1 class="cover-title"><span class="accent">TITLE</span> PROJECT</h1>
  <p class="cover-sub">subtext <span class="accent">presentation</span></p>
  <div class="brand"><span class="brand-mark"></span><span class="brand-name">Amber Harbor Guild</span></div>
  <div class="band">
    <svg class="arrow prev" viewBox="0 0 44 80"><polygon points="44,0 44,18 22,40 44,62 44,80 0,40" fill="#fff"/></svg>
    <p class="byline">Presentation by<strong>Daniel Reyes</strong></p>
    <svg class="arrow next" viewBox="0 0 44 80"><polygon points="0,0 0,18 22,40 0,62 0,80 44,40" fill="#fff"/></svg>
  </div>
</section>

<section class="slide about col-right row-1">
  <h2 class="slide-title"><span class="accent">About</span> Company</h2>
  <div class="about-body">
    <p><b>Lorem ipsum</b> dolor sit amet, consectetuer adipiscing elit. Maecenas porttitor congue massa. Fusce posuere, magna sed pulvinar ultricies, purus lectus malesuada libero, sit amet commodo magna eros quis urna.</p>
    <p><b>Nunc viverra imperdiet enim</b>. Fusce est. Vivamus a tellus. Pellentesque habitant morbi tristique senectus et netus et malesuada fames ac turpis egestas. Proin pharetra nonummy pede. Mauris et orci.</p>
    <p><b>Aenean nec lorem.</b> In porttitor. Donec laoreet nonummy augue.</p>
    <p>Suspendisse dui purus, scelerisque at, vulputate vitae, pretium mattis, nunc. Mauris eget neque at sem venenatis eleifend. Ut nonummy.</p>
    <p><b>Fusce aliquet pede non pede.</b><br>Suspendisse dapibus lorem pellentesque magna. Integer nulla.</p>
  </div>
  <footer class="footer">
    <svg class="chev prev" viewBox="0 0 10 16"><polygon points="10,0 10,4 5,8 10,12 10,16 0,8" fill="#9a9a9a"/></svg>
    <div class="footer-tab"><span class="dot"></span><span class="name">Amber Harbor Guild</span></div>
    <svg class="chev next" viewBox="0 0 10 16"><polygon points="0,0 0,4 5,8 0,12 0,16 10,8" fill="#9a9a9a"/></svg>
  </footer>
</section>

<section class="slide services col-left row-2">
  <h2 class="slide-title"><span class="accent">Our</span> Services</h2>
  <ul class="service-list">
    <li>Lorem ipsum</li><li>Lorem ipsum</li><li>Lorem ipsum</li><li>Lorem ipsum</li><li>Lorem ipsum</li>
    <li>Lorem ipsum</li><li>Lorem ipsum</li><li>Lorem ipsum</li><li>Lorem ipsum</li><li>Lorem ipsum</li>
  </ul>
  <div class="team-photo" role="img" aria-label="Photo of a team of eight business people in dark suits standing together"></div>
  <footer class="footer">
    <svg class="chev prev" viewBox="0 0 10 16"><polygon points="10,0 10,4 5,8 10,12 10,16 0,8" fill="#9a9a9a"/></svg>
    <div class="footer-tab"><span class="dot"></span><span class="name">Amber Harbor Guild</span></div>
    <svg class="chev next" viewBox="0 0 10 16"><polygon points="0,0 0,4 5,8 0,12 0,16 10,8" fill="#9a9a9a"/></svg>
  </footer>
</section>

<section class="slide table-slide col-right row-2">
  <h2 class="slide-title"><span class="accent">Table</span> Presentation</h2>
  <table class="data-table">
    <colgroup><col class="c1"><col class="c2"><col class="c3"></colgroup>
    <thead><tr><th class="cat">CATEGORY</th><th class="opt1">OPTION 1</th><th class="opt2">OPTION 2</th></tr></thead>
    <tbody>
      <tr class="group"><td colspan="3">Category 1</td></tr>
      <tr><td class="label">Lorem ipsum dolor sit amet</td><td class="yes">Yes</td><td class="no">-</td></tr>
      <tr class="alt"><td class="label">Lorem ipsum dolor sit amet</td><td class="yes">Yes</td><td class="no">-</td></tr>
      <tr><td class="label">Lorem ipsum dolor sit amet</td><td class="yes">Yes</td><td class="no">-</td></tr>
      <tr class="group"><td colspan="3">Category 2</td></tr>
      <tr><td class="label">Lorem ipsum dolor sit amet</td><td class="yes">Yes</td><td class="no">-</td></tr>
      <tr class="alt"><td class="label">Lorem ipsum dolor sit amet</td><td class="yes">Yes</td><td class="no">-</td></tr>
      <tr><td class="label">Lorem ipsum dolor sit amet</td><td class="yes">Yes</td><td class="no">-</td></tr>
      <tr class="alt"><td class="label">Lorem ipsum dolor sit amet</td><td class="yes">Yes</td><td class="no">-</td></tr>
      <tr class="group"><td colspan="3">Category 3</td></tr>
      <tr><td class="label">Lorem ipsum dolor sit amet</td><td class="yes">Yes</td><td class="no">-</td></tr>
      <tr class="alt"><td class="label">Lorem ipsum dolor sit amet</td><td class="yes">Yes</td><td class="no">-</td></tr>
    </tbody>
  </table>
  <footer class="footer">
    <svg class="chev prev" viewBox="0 0 10 16"><polygon points="10,0 10,4 5,8 10,12 10,16 0,8" fill="#9a9a9a"/></svg>
    <div class="footer-tab"><span class="dot"></span><span class="name">Amber Harbor Guild</span></div>
    <svg class="chev next" viewBox="0 0 10 16"><polygon points="0,0 0,4 5,8 0,12 0,16 10,8" fill="#9a9a9a"/></svg>
  </footer>
</section>

<section class="slide contact col-left row-3">
  <h2 class="slide-title"><span class="accent">Contact</span> Info</h2>
  <div class="map" role="img" aria-label="Map of Eastern Europe and the Black Sea region"></div>
  <div class="contact-body">
    <p class="lead"><b>Lorem ipsum</b> dolor sit amet, consectetuer adipiscing elit. Maecenas porttitor congue massa. Fusce posuere, magna sed pulvinar ultricies, purus lectus malesuada libero, sit amet commodo magna eros quis urna.</p>
    <h4>Address</h4>
    <p>1234 Street Address<br>New York, America<br>67890 (U.S.A)</p>
    <h4>Phone</h4>
    <p>0123-456-789</p>
    <h4>FAX</h4>
    <p>0123-456-789</p>
    <h4>Email</h4>
    <p>info@yourcompany.com</p>
    <h4>Website</h4>
    <p>www.yourcompany.com</p>
  </div>
  <div class="social">
    <span class="sq"></span><span class="sq"></span><span class="sq"></span><span class="sq"></span>
    <span class="handle">@YOUR<span>COMPANY</span></span>
  </div>
  <footer class="footer">
    <svg class="chev prev" viewBox="0 0 10 16"><polygon points="10,0 10,4 5,8 10,12 10,16 0,8" fill="#9a9a9a"/></svg>
    <div class="footer-tab"><span class="dot"></span><span class="name">Amber Harbor Guild</span></div>
    <svg class="chev next" viewBox="0 0 10 16"><polygon points="0,0 0,4 5,8 0,12 0,16 10,8" fill="#9a9a9a"/></svg>
  </footer>
</section>

<section class="slide closing col-right row-3">
  <h2 class="thanks">Thank<span class="accent">You</span></h2>
  <div class="brand"><span class="brand-mark"></span><span class="brand-name">Amber Harbor Guild</span></div>
  <div class="band">
    <svg class="arrow prev" viewBox="0 0 44 80"><polygon points="44,0 44,18 22,40 44,62 44,80 0,40" fill="#fff"/></svg>
    <p class="byline">Presentation by<strong>Daniel Reyes</strong></p>
    <svg class="arrow next" viewBox="0 0 44 80"><polygon points="0,0 0,18 22,40 0,62 0,80 44,40" fill="#fff"/></svg>
  </div>
</section>

</body>
</html>
```